8 Page Publishing/Entertainment Website Design

We need a slick, polished, professional looking fully mobile responsive website designed for the publishing / entertainment industry. It will contain 8 pages, including the Home page. The site is to be designed in pure HTML and CSS only and to be compatible with any type of server we put it on. Pages are *not* to be part of any template system, like WordPress or others like it. Pure HTML and CSS standalone pages only. No WordPress or Joomla, etc. Website to use our logo's colors of red/white throughout its design. Uploaded files contain a word DOC that outlines more of our needs and we have included our logo file. Please read the specifications in the Word Document attached. We have also included a PDF file with the website specs as well.

Target Market(s)

Authors and Screenwriters

Coding

Coded - Design and coding required

Number of Pages Required

5+ page

Colors
ec1f27
ffffff
f04a50
f59195

Requirements
Must have
• The site is to be designed in pure HTML and CSS only and to be compatible with any type of server we put it on. Pages are *not* to be part of any template system, like WordPress or others like it. Pure HTML and CSS standalone pages only. No WordPress or Joomla, etc. Website to use our logo's colors of red/white throughout its design. Uploaded files contain a word DOC that outlines more of our needs and we have included our logo file. Please read the specifications in the Word Document attached. We have also included a PDF file with the website specs as well.
Should not have
• No Wordpress or other Template type pages. Pure HTML and CSS only. Some Javascript and JQuery is okay, upon approval.

```html
<!DOCTYPE html>
<html lang="en">
<head>
<meta charset="utf-8">
<title>Keystone Ink Publishing</title>
<link href="https://fonts.googleapis.com/css2?family=Montserrat:wght@400;600;700;800&family=Open+Sans:ital,wght@0,400;0,600;0,700;1,400&display=swap" rel="stylesheet">
<style>
:root{
  --red:#ec1f27;
  --red-soft:#f04a50;
  --pink:#f59195;
  --white:#ffffff;
  --ink:#2b2b2b;
  --text:#6d6d6d;
  --muted:#9a9a9a;
  --line:#e6e6e6;
  --dark:#3b3b3b;
  --darker:#2f2f2f;
  --footer:#3f3f3f;
}
*{box-sizing:border-box;margin:0;padding:0}
html,body{width:1200px;height:5373px;overflow:hidden}
body{background:var(--white);font-family:"Open Sans",Arial,sans-serif;color:var(--text);position:relative}
.abs{position:absolute}
h1,h2,h3,h4,.head{font-family:"Montserrat",Arial,sans-serif}
.btn{position:absolute;display:flex;align-items:center;justify-content:center;border-radius:20px;font-family:"Montserrat",Arial,sans-serif;font-weight:700;font-size:12px;letter-spacing:.5px;color:var(--white);text-transform:uppercase}
.btn-red{background:var(--red)}
.btn-dark{background:var(--dark);font-size:10px}
.ph{position:absolute}
p{font-size:12px;line-height:19px}

/* header */
.site-header{position:absolute;left:0;top:0;width:1200px;height:79px;background:var(--white);border-top:4px solid var(--red);box-shadow:0 2px 6px rgba(0,0,0,.08);z-index:2}
.brand{position:absolute;left:150px;top:8px;display:flex;align-items:center;gap:10px}
.brand-mark{width:58px;height:58px;border-radius:50%;background:var(--red)}
.brand-name{font-family:"Montserrat",sans-serif;font-weight:800;font-size:13px;color:var(--red);line-height:15px;width:110px}
.main-nav{position:absolute;left:430px;top:22px;display:flex;gap:28px}
.main-nav a{font-family:"Montserrat",sans-serif;font-size:11px;font-weight:600;color:var(--ink);text-decoration:none;text-transform:uppercase}
.main-nav a.active{color:var(--red)}

/* hero */
.hero{position:absolute;left:0;top:79px;width:1200px;height:421px;background:linear-gradient(180deg,#545454,#3d3d3d)}
.hero-video{left:322px;top:15px;width:556px;height:304px;background:linear-gradient(135deg,#7a5a44,#4b3b33 50%,#8a6e58);border:8px solid #5c5c5c}
.play{position:absolute;border-radius:50%;background:var(--red);display:flex;align-items:center;justify-content:center}
.play svg{display:block}

/* recent posts strip */
.post-strip{position:absolute;left:0;top:500px;width:1200px;height:175px;background:var(--white)}
.mini-post{position:absolute;top:50px;display:flex;gap:12px;width:280px}
.mini-thumb{width:82px;height:78px;background:linear-gradient(135deg,#c9b8a6,#8d7a6a);flex:none}
.mini-post h4{font-family:"Open Sans",sans-serif;font-size:12px;font-weight:400;color:var(--ink);line-height:17px}
.meta{font-size:10px;color:var(--muted);margin-top:8px}
.meta b{color:var(--red);font-weight:400}

/* news */
.news{position:absolute;left:0;top:734px;width:1200px;height:540px}
.news-bar{position:absolute;left:161px;top:0;width:537px;height:30px;border-bottom:1px solid var(--line);display:flex;align-items:center}
.news-tag{background:var(--red);color:var(--white);font-family:"Montserrat",sans-serif;font-weight:700;font-size:10px;height:30px;padding:0 12px;display:flex;align-items:center}
.news-ticker{font-size:10px;color:var(--muted);padding-left:14px;flex:1}
.news-arrows{display:flex;gap:10px;padding-right:8px;font-size:12px;color:var(--ink)}
.news-feature{left:161px;top:46px;width:537px;height:400px;background:linear-gradient(135deg,#5b6f7a,#c9b49a 55%,#2f3b45)}
.news-caption{position:absolute;left:28px;bottom:26px;width:360px;color:var(--white)}
.news-caption h3{font-family:"Open Sans",sans-serif;font-size:19px;font-weight:700;line-height:24px}
.news-caption span{font-size:10px;opacity:.8}
.news-corner{position:absolute;right:10px;bottom:10px;width:26px;height:26px;background:var(--red)}
.news-thumbs{position:absolute;left:161px;top:452px;width:537px;display:flex;gap:6px}
.news-thumbs div{flex:1;height:58px;background:linear-gradient(135deg,#b8a793,#6c5c51)}
.news-thumbs div:nth-child(2){background:linear-gradient(135deg,#8a8f95,#434a52)}
.news-thumbs div:nth-child(4){background:linear-gradient(135deg,#c8a88c,#7d5e46)}
.side-tabs{position:absolute;left:734px;top:0;width:312px;height:30px;display:flex;border-bottom:1px solid var(--line)}
.side-tabs span{flex:1;text-align:center;font-family:"Montserrat",sans-serif;font-size:10px;font-weight:600;color:var(--muted);line-height:30px}
.side-tabs span.on{background:var(--dark);color:var(--white)}
.side-item{position:absolute;left:734px;width:312px;display:flex;gap:12px;padding-bottom:14px;border-bottom:1px solid var(--line)}
.side-thumb{width:94px;height:80px;flex:none;background:linear-gradient(135deg,#a9a39a,#5e5a55)}
.side-item h4{font-family:"Open Sans",sans-serif;font-size:12px;font-weight:400;color:var(--ink);margin-top:4px}

/* video band */
.video-band{position:absolute;left:0;top:1318px;width:1200px;height:222px;display:flex}
.video-tile{position:relative;width:300px;height:222px}
.video-tile .play{left:122px;top:62px;width:56px;height:56px;background:rgba(236,31,39,.85);border:2px solid rgba(255,255,255,.6)}
.video-tile p{position:absolute;left:18px;bottom:22px;width:250px;color:var(--white);font-size:11px;line-height:15px}

/* section titles */
.sec-title{position:absolute;left:0;width:1200px;text-align:center}
.sec-title .kicker{font-family:"Montserrat",sans-serif;font-weight:700;font-size:22px;color:var(--red);text-transform:uppercase}
.sec-title h2{font-family:"Montserrat",sans-serif;font-weight:700;font-size:24px;color:var(--ink);text-transform:uppercase;margin-top:2px}
.sec-title p{width:720px;margin:14px auto 0;font-size:11px;line-height:17px;color:var(--muted)}

/* about */
.about{position:absolute;left:0;top:1612px;width:1200px;height:700px}
.about-card{position:absolute;top:143px;width:401px}
.about-photo{width:401px;height:280px;background:linear-gradient(135deg,#d9d4cf,#7c7166)}
.about-card h4{font-family:"Open Sans",sans-serif;font-size:13px;font-weight:400;color:var(--ink);margin:16px 0 8px;line-height:19px}
.about-card p{font-size:11px;line-height:17px;color:var(--muted)}

/* features */
.feature{position:absolute;left:0;width:1200px;height:287px}
.feature-num{position:absolute;top:0;height:287px;display:flex;align-items:center;justify-content:center;font-family:"Montserrat",sans-serif;font-weight:400;font-size:60px}
.feature-img{position:absolute;top:0;height:287px}
.feature-text{position:absolute;top:10px;width:330px;text-align:center}
.feature-text .kick{font-family:"Montserrat",sans-serif;font-weight:700;font-size:11px;color:var(--red);text-transform:uppercase}
.feature-text h3{font-family:"Montserrat",sans-serif;font-weight:700;font-size:22px;color:var(--ink);text-transform:uppercase;margin:4px 0 14px}
.feature-text p{font-size:11px;line-height:17px;color:var(--muted);margin-bottom:12px;text-align:left}

/* testimonials */
.testimonials{position:absolute;left:0;top:3080px;width:1200px;height:305px;background:linear-gradient(180deg,var(--red),var(--red-soft))}
.t-label{position:absolute;left:465px;top:50px;width:270px;height:24px;background:var(--darker);color:var(--white);font-family:"Montserrat",sans-serif;font-weight:700;font-size:11px;text-align:center;line-height:24px;text-transform:uppercase}
.t-title{position:absolute;left:0;top:74px;width:1200px;text-align:center;font-family:"Montserrat",sans-serif;font-weight:800;font-size:40px;color:var(--white)}
.quote-card{position:absolute;top:160px;width:430px;height:160px;background:#fde8e9;border:6px solid rgba(255,255,255,.5);display:flex;gap:20px;padding:24px 24px 0}
.avatar{width:88px;height:88px;border-radius:50%;background:linear-gradient(135deg,#c7b3a3,#6b5a4d);flex:none;border:4px solid var(--white)}
.quote-card p{font-style:italic;font-size:11px;line-height:17px;color:var(--text)}
.quote-card .who{font-style:italic;font-size:11px;color:var(--ink);margin-top:10px}

/* authors */
.authors{position:absolute;left:0;top:3492px;width:1200px;height:620px}
.author{position:absolute;top:180px;width:268px;text-align:center}
.author-photo{width:268px;height:232px}
.author h4{font-family:"Montserrat",sans-serif;font-weight:600;font-size:14px;color:var(--ink);margin:22px 0 8px;text-transform:uppercase}
.author p{font-size:11px;line-height:16px;color:var(--muted);width:240px;margin:0 auto}
.socials{display:flex;gap:6px;justify-content:center;margin-top:12px}
.socials span{width:18px;height:18px;background:var(--dark);border-radius:2px}
.author .btn{position:relative;margin:16px auto 0;width:96px;height:24px}

/* guarantee */
.guarantee{position:absolute;left:0;top:4112px;width:1200px;height:251px;background:linear-gradient(90deg,var(--pink),var(--red-soft) 60%,var(--red));overflow:hidden}
.guarantee .small{position:absolute;left:161px;top:60px;font-family:"Montserrat",sans-serif;font-weight:600;font-size:14px;color:var(--white);text-transform:uppercase}
.guarantee h2{position:absolute;left:161px;top:80px;font-family:"Montserrat",sans-serif;font-weight:800;font-size:30px;color:var(--white);text-transform:uppercase}
.guarantee p{position:absolute;left:161px;top:130px;width:560px;font-size:11px;line-height:16px;color:var(--white)}
.halo{position:absolute;border-radius:50%;background:rgba(255,255,255,.12)}
.seal{position:absolute;left:870px;top:40px;width:170px;height:170px;border-radius:50%;background:#e0a93a;border:10px solid #f3cd6a}

/* press */
.press{position:absolute;left:0;top:4525px;width:1200px;height:60px;display:flex;justify-content:center;gap:70px;align-items:center}
.press span{font-family:"Montserrat",sans-serif;font-size:24px;color:#5a5a5a;font-weight:600}
.press span.light{font-weight:400;color:#8a8a8a}

/* map */
.map{position:absolute;left:0;top:4621px;width:1200px;height:286px;background:linear-gradient(135deg,#ececec,#dcdcdc 50%,#e8e8e8)}

/* footer */
.site-footer{position:absolute;left:0;top:4907px;width:1200px;height:466px;background:var(--footer);color:#cfcfcf}
.contact-col{position:absolute;top:52px;width:300px;text-align:center;font-size:11px}
.contact-col svg{display:block;margin:0 auto 12px}
.foot-social{position:absolute;left:0;top:170px;width:1200px;display:flex;justify-content:center;gap:10px}
.foot-social span{width:30px;height:30px;background:#5a5a5a;border-radius:3px}
.subscribe{position:absolute;left:355px;top:250px;display:flex}
.subscribe .field{width:370px;height:36px;background:var(--white);font-size:11px;color:var(--muted);line-height:36px;padding-left:14px}
.subscribe .go{width:120px;height:36px;background:var(--red);color:var(--white);font-family:"Montserrat",sans-serif;font-weight:700;font-size:12px;text-align:center;line-height:36px}
.foot-nav{position:absolute;left:0;top:350px;width:1200px;display:flex;justify-content:center;gap:24px}
.foot-nav a{font-family:"Montserrat",sans-serif;font-size:10px;color:#dcdcdc;text-decoration:none;text-transform:uppercase}
.copyright{position:absolute;left:0;bottom:0;width:1200px;height:54px;background:var(--red);color:var(--white);text-align:center;font-size:10px;line-height:54px}
</style>
</head>
<body>

<header class="site-header">
  <div class="brand"><span class="brand-mark"></span><span class="brand-name">KEYSTONE INK PUBLISHING</span></div>
  <nav class="main-nav">
    <a class="active" href="#">Home</a><a href="#">About KIP</a><a href="#">Apply Now</a><a href="#">New Results</a><a href="#">Our Authors</a><a href="#">FAQ</a><a href="#">News</a><a href="#">Contact Us</a>
  </nav>
</header>

<section class="hero">
  <div class="ph hero-video" role="img" aria-label="Video still of shelves stacked with books and records">
    <span class="play" style="left:240px;top:115px;width:62px;height:62px"><svg width="22" height="24" viewBox="0 0 22 24"><path d="M2 1l19 11L2 23z" fill="#fff"/></svg></span>
  </div>
  <a class="btn btn-red" style="left:515px;top:341px;width:170px;height:40px">Apply Now</a>
</section>

<section class="post-strip">
  <article class="mini-post" style="left:161px"><div class="mini-thumb" role="img" aria-label="Author portrait photo"></div><div><h4>Etiam euismod odio id ante malesuada viverra</h4><div class="meta"><b>August 2019</b> · 2 comments</div></div></article>
  <article class="mini-post" style="left:458px"><div class="mini-thumb" role="img" aria-label="Author portrait photo"></div><div><h4>Etiam euismod odio id ante malesuada viverra</h4><div class="meta"><b>August 2019</b> · 2 comments</div></div></article>
  <article class="mini-post" style="left:770px"><div class="mini-thumb" role="img" aria-label="Author portrait photo"></div><div><h4>Etiam euismod odio id ante malesuada viverra</h4><div class="meta"><b>August 2019</b> · 2 comments</div></div></article>
</section>

<section class="news">
  <div class="news-bar"><span class="news-tag">NEWS FLASH</span><span class="news-ticker">Ut aliquet tellus vitae dignissim vehicula</span><span class="news-arrows">‹ ›</span></div>
  <div class="ph news-feature" role="img" aria-label="Person reading a stack of magazines">
    <div class="news-caption"><h3>Retirees, It May Be Time To Get Your Head Out Of The Sand</h3><span>By John Doe · 26 August</span></div>
    <span class="news-corner"></span>
  </div>
  <div class="news-thumbs" role="img" aria-label="Row of related story photos"><div></div><div></div><div></div><div></div><div></div></div>
  <div class="side-tabs"><span class="on">TRENDING</span><span>COMMENTS</span><span>LATEST</span></div>
  <div class="side-item" style="top:46px"><div class="side-thumb" role="img" aria-label="Story photo"></div><div><h4>Consectetur ac eleifend eget</h4><div class="meta">26th August 2019</div></div></div>
  <div class="side-item" style="top:160px"><div class="side-thumb" role="img" aria-label="Story photo"></div><div><h4>Consectetur ac eleifend eget</h4><div class="meta">26th August 2019</div></div></div>
  <div class="side-item" style="top:274px"><div class="side-thumb" role="img" aria-label="Story photo"></div><div><h4>Consectetur ac eleifend eget</h4><div class="meta">26th August 2019</div></div></div>
  <div class="side-item" style="top:388px;border:0"><div class="side-thumb" role="img" aria-label="Story photo"></div><div><h4>Consectetur ac eleifend eget</h4><div class="meta">26th August 2019</div></div></div>
</section>

<section class="video-band">
  <div class="video-tile" role="img" aria-label="Video still of a writer at a laptop" style="background:linear-gradient(135deg,#5c6670,#2e343a)"><span class="play"><svg width="16" height="18" viewBox="0 0 22 24"><path d="M2 1l19 11L2 23z" fill="#fff"/></svg></span><p>Eget malesuada arcu dapibus et, mauris fringilla ligula convallis pharetra.</p></div>
  <div class="video-tile" role="img" aria-label="Video still of an author signing books" style="background:linear-gradient(135deg,#c7343a,#7d1b20)"><span class="play"><svg width="16" height="18" viewBox="0 0 22 24"><path d="M2 1l19 11L2 23z" fill="#fff"/></svg></span><p>Eget malesuada arcu dapibus et, mauris fringilla ligula convallis pharetra.</p></div>
  <div class="video-tile" role="img" aria-label="Video still of a reading event" style="background:linear-gradient(135deg,#5a4b48,#2a2424)"><span class="play"><svg width="16" height="18" viewBox="0 0 22 24"><path d="M2 1l19 11L2 23z" fill="#fff"/></svg></span><p>Eget malesuada arcu dapibus et, mauris fringilla ligula convallis pharetra.</p></div>
  <div class="video-tile" role="img" aria-label="Video still of a screenwriter at work" style="background:linear-gradient(135deg,var(--red-soft),#b81a20)"><span class="play"><svg width="16" height="18" viewBox="0 0 22 24"><path d="M2 1l19 11L2 23z" fill="#fff"/></svg></span><p>Eget malesuada arcu dapibus et, mauris fringilla ligula convallis pharetra.</p></div>
</section>

<section class="about">
  <div class="sec-title" style="top:18px"><div class="kicker">About</div><h2>Keystone Ink Publishing</h2><p>Phasellus quis ligula consectetur, eleifend dolor id, posuere sem. Nunc in diam aliquet, feugiat nisl eget, interdum metus. Sed id accumsan est, vitae ultrices dolor. Nam a mauris quis massa blandit aliquam.</p></div>
  <div class="about-card" style="left:161px"><div class="about-photo" role="img" aria-label="Portrait of a founder in a dark suit"></div><h4>Maecenas cursus bibendum dictum. Vivamus efficitur eget ipsum at fermentum</h4><p>Lorem ipsum dolor sit amet, consectetur adipiscing elit. In et erat ante. Ut posuere nibh et pulvinar malesuada, sed ornare diam. Nulla eu felis eleifend, tincidunt nunc ac, accumsan est. Aliquam egestas, elit a tempor dictum.</p></div>
  <div class="about-card" style="left:638px"><div class="about-photo" role="img" aria-label="Portrait of a co-founder in a grey suit" style="background:linear-gradient(135deg,#b9bcc2,#4c4f56)"></div><h4>Maecenas cursus bibendum dictum. Vivamus efficitur eget ipsum at fermentum</h4><p>Lorem ipsum dolor sit amet, consectetur adipiscing elit. In et erat ante. Ut posuere nibh et pulvinar malesuada, sed ornare diam. Nulla eu felis eleifend, tincidunt nunc ac, accumsan est. Aliquam egestas, elit a tempor dictum.</p></div>
  <a class="btn btn-red" style="left:473px;top:608px;width:254px;height:36px">Click Here For Details</a>
</section>

<section class="feature" style="top:2335px">
  <div class="feature-num" style="left:0;width:161px;background:var(--pink);color:rgba(255,255,255,.55)">01</div>
  <div class="feature-img" role="img" aria-label="Hands leafing through an open magazine" style="left:161px;width:477px;background:linear-gradient(135deg,#e5ddd5,#a89482)"></div>
  <div class="feature-text" style="left:714px"><div class="kick">Aliquam ultrices urna id</div><h3>Etiam Euismod Odio</h3><p>Lorem ipsum dolor sit amet, consectetur adipiscing elit. In et erat ante. Ut posuere nibh et pulvinar malesuada. Nulla eu felis eleifend, tincidunt nunc ac, accumsan est sed ornare.</p><p>Lorem ipsum dolor sit amet, consectetur adipiscing elit. In et erat ante. Ut posuere nibh et pulvinar malesuada.</p><a class="btn btn-dark" style="position:relative;display:flex;margin:0 auto;width:84px;height:22px">Learn More</a></div>
</section>

<section class="feature" style="top:2715px">
  <div class="feature-text" style="left:180px"><div class="kick">Aliquam leo odio elementum</div><h3>Donec Ullamcorper Enim</h3><p>Lorem ipsum dolor sit amet, consectetur adipiscing elit. In et erat ante. Ut posuere nibh et pulvinar malesuada. Nulla eu felis eleifend, tincidunt nunc ac, accumsan est sed ornare.</p><p>Lorem ipsum dolor sit amet, consectetur adipiscing elit. In et erat ante. Ut posuere nibh et pulvinar malesuada.</p><a class="btn btn-dark" style="position:relative;display:flex;margin:0 auto;width:84px;height:22px">Learn More</a></div>
  <div class="feature-img" role="img" aria-label="Coffee cup on a desk beside magazines" style="left:562px;width:477px;background:linear-gradient(135deg,#d8cfc8,#6f6761 50%,#c7b9ae)"></div>
  <div class="feature-num" style="left:1039px;width:161px;background:#5a5a5a;color:rgba(255,255,255,.35)">02</div>
</section>

<section class="testimonials">
  <div class="t-label">What Keystone Ink Publishing</div>
  <div class="t-title">HAVE TO SAY</div>
  <div class="quote-card" style="left:161px"><div class="avatar" role="img" aria-label="Client portrait"></div><div><p>Vestibulum vitae erat. Morbi ut ex et justo tristique aliquet ut vel tortor. Donec eu mauris molestie, feugiat nulla quis, consequat dolor elementum ultrices.</p><div class="who">Ray Holden</div></div></div>
  <div class="quote-card" style="left:609px"><div class="avatar" role="img" aria-label="Client portrait"></div><div><p>Vestibulum vitae erat. Morbi ut ex et justo tristique aliquet ut vel tortor. Donec eu mauris molestie, feugiat nulla quis, consequat dolor elementum ultrices.</p><div class="who">Ray Holden</div></div></div>
</section>

<section class="authors">
  <div class="sec-title" style="top:0"><div class="kicker">Top Authors Use</div><h2>Keystone Ink Publishing</h2><p>Phasellus quis ligula consectetur, eleifend dolor id, posuere sem. Nunc in diam aliquet, feugiat nisl eget, interdum metus. Sed id accumsan est, vitae ultrices dolor. Nam a mauris quis massa blandit aliquam.</p></div>
  <div class="author" style="left:161px"><div class="author-photo" role="img" aria-label="Portrait of an author at her desk" style="background:linear-gradient(135deg,#6b3b36,#2d1e1c)"></div><h4>Nora Vale</h4><p>Donec ullamcorper enim in nulla posuere, eget dapibus lorem tempus. Integer magna elit, bibendum in justo eget.</p><div class="socials"><span></span><span></span><span></span><span></span></div><a class="btn btn-dark">View Profile</a></div>
  <div class="author" style="left:466px"><div class="author-photo" role="img" aria-label="Portrait of a bearded author" style="background:linear-gradient(135deg,#8a7668,#2f2622)"></div><h4>Dale Corwin</h4><p>Donec ullamcorper enim in nulla posuere, eget dapibus lorem tempus. Integer magna elit, bibendum in justo eget.</p><div class="socials"><span></span><span></span><span></span><span></span></div><a class="btn btn-dark">View Profile</a></div>
  <div class="author" style="left:770px"><div class="author-photo" role="img" aria-label="Portrait of an author in a hat" style="background:linear-gradient(135deg,#c9b9a4,#3b2f28)"></div><h4>Dale Corwin</h4><p>Donec ullamcorper enim in nulla posuere, eget dapibus lorem tempus. Integer magna elit, bibendum in justo eget.</p><div class="socials"><span></span><span></span><span></span><span></span></div><a class="btn btn-dark">View Profile</a></div>
</section>

<section class="guarantee">
  <span class="halo" style="left:800px;top:-60px;width:320px;height:320px"></span>
  <span class="halo" style="left:850px;top:-10px;width:220px;height:220px"></span>
  <div class="small">I know you'll be happy with our</div>
  <h2>Work. In Fact, I Guarantee It.</h2>
  <p>Vivamus tempus in dolor porttitor, rhoncus lorem ut, pulvinar sem. Curabitur ac dapibus nisi. Nam et vestibulum ex, vitae dignissim lectus. Maecenas quis urna sed justo tincidunt vulputate. Sed non tincidunt nulla, id finibus est lorem.</p>
  <span class="seal"></span>
</section>

<section class="press">
  <span>Foundermade</span><span>tradehall.net</span><span class="light">Penwright Daily</span><span>Shelfstarter</span>
</section>

<div class="map" role="img" aria-label="Street map showing the office location"></div>

<footer class="site-footer">
  <div class="contact-col" style="left:150px"><svg width="24" height="24" viewBox="0 0 24 24"><path d="M6 2l4 5-2 3c1 3 3 5 6 6l3-2 5 4-2 4C11 22 2 13 2 4z" fill="#fff"/></svg>(555) 240-7146</div>
  <div class="contact-col" style="left:450px"><svg width="26" height="20" viewBox="0 0 26 20"><rect x="1" y="1" width="24" height="18" fill="none" stroke="#fff" stroke-width="2"/><path d="M1 1l12 10L25 1" fill="none" stroke="#fff" stroke-width="2"/></svg>hello@keystoneink.example</div>
  <div class="contact-col" style="left:750px"><svg width="20" height="26" viewBox="0 0 20 26"><path d="M10 1a9 9 0 0 0-9 9c0 7 9 15 9 15s9-8 9-15a9 9 0 0 0-9-9z" fill="#fff"/><circle cx="10" cy="10" r="3.5" fill="#3f3f3f"/></svg>4120 Birch Street, Suite 18, Rivermont, IL 60000</div>
  <div class="foot-social"><span></span><span></span><span></span><span></span></div>
  <div class="subscribe"><span class="field">Enter your email address</span><span class="go">SUBSCRIBE</span></div>
  <nav class="foot-nav"><a href="#">Home</a><a href="#">About KIP</a><a href="#">Apply Now</a><a href="#">New Results</a><a href="#">Our Authors</a><a href="#">FAQ</a><a href="#">News</a><a href="#">Contact Us</a></nav>
  <div class="copyright">© 2019 Keystone Ink Publishing · All Rights Reserved</div>
</footer>

</body>
</html>
```